Tallgrove Vale Management

I need a professional website. My current website is tallgrovevalemanagement.com and I hate it. It was created with some AI tool very quickly because I needed a site up and running with no advanced notice. I’m open to all designs .. I trust you, the professionals will deliver the results I’m anxiously awaiting! :)

```html
<!DOCTYPE html>
<html lang="en">
<head>
<meta charset="utf-8">
<title>Tallgrove Vale Management</title>
<link href="https://fonts.googleapis.com/css2?family=Poppins:wght@500;600;700;800&family=Inter:wght@400;500;600&display=swap" rel="stylesheet">
<style>
:root{
  --navy:#0f1f3d;
  --navy-2:#16294d;
  --red:#c8102e;
  --ink:#1b2333;
  --muted:#5d6576;
  --line:#e3e6ec;
  --soft:#f4f5f8;
  --white:#fff;
}
*{box-sizing:border-box;margin:0;padding:0}
html,body{width:1200px;height:3008px;overflow:hidden}
body{font-family:"Inter",sans-serif;color:var(--ink);background:var(--white);font-size:13px;line-height:1.5;position:relative}
h1,h2,h3,h4,.brand,.btn,.stat b,.step b{font-family:"Poppins",sans-serif}
.sec{position:absolute;left:0;width:1200px}
.btn{display:inline-flex;align-items:center;justify-content:center;height:42px;padding:0 22px;font-size:11px;font-weight:700;letter-spacing:.5px;text-transform:uppercase;border-radius:3px}
.btn-red{background:var(--red);color:#fff}
.btn-navy{background:var(--navy);color:#fff}
.btn-ghost{border:1.5px solid var(--navy);color:var(--navy);background:#fff}
.btn-outline-w{border:1.5px solid #fff;color:#fff}
.label{font-size:10px;font-weight:700;letter-spacing:1px;text-transform:uppercase;color:var(--red)}
.photo{position:absolute}
.center{text-align:center}

/* header */
.header{top:0;height:80px;background:#fff;border-bottom:1px solid var(--line);z-index:3}
.logo-box{position:absolute;left:40px;top:0;width:120px;height:112px;background:var(--navy);display:flex;flex-direction:column;align-items:center;justify-content:center;gap:6px;border-bottom:4px solid var(--red)}
.logo-box .sq{width:16px;height:16px;background:var(--red)}
.brand{color:#fff;font-weight:700;font-size:14px;letter-spacing:1px;text-align:center;line-height:1.15}
.nav{position:absolute;left:300px;top:0;height:80px;display:flex;gap:38px;align-items:center;font-weight:600;font-size:13px}
.nav a{color:var(--ink);position:relative}
.nav a.on{color:var(--red)}
.nav a.on:after{content:"";position:absolute;left:0;right:0;bottom:-8px;height:2px;background:var(--red)}
.head-right{position:absolute;right:40px;top:19px;display:flex;gap:22px;align-items:center;font-weight:700;font-size:13px;font-family:"Poppins",sans-serif}
.ico-phone{display:inline-flex;align-items:center;gap:8px}

/* hero */
.hero{top:80px;height:610px;background:linear-gradient(90deg,#fff 0,#fff 46%,#f2f3f6 100%)}
.hero-photo{left:560px;top:0;width:640px;height:500px;background:linear-gradient(180deg,#b9d4ee 0,#d9e6f2 30%,#c9b5a3 60%,#8f7766 100%)}
.hero-copy{position:absolute;left:40px;top:70px;width:500px}
.pill{display:inline-block;background:var(--red);color:#fff;font-size:9px;font-weight:700;letter-spacing:1px;padding:6px 12px;border-radius:2px;text-transform:uppercase}
.hero h1{font-size:40px;line-height:1.12;font-weight:800;color:var(--navy);margin-top:20px}
.hero h1 span{color:var(--red)}
.hero p{color:var(--muted);margin-top:18px;font-size:13.5px;max-width:430px}
.hero .ctas{display:flex;gap:14px;margin-top:26px}
.badges{display:flex;gap:22px;margin-top:30px;font-size:9px;font-weight:700;text-transform:uppercase;color:var(--navy)}
.badges span{display:flex;align-items:center;gap:6px}
.badges i{width:14px;height:14px;border-radius:50%;background:var(--red);display:inline-block}
.trusted{position:absolute;left:40px;top:510px;width:500px}
.trusted h4{font-size:13px;color:var(--navy)}
.partners{display:flex;gap:34px;margin-top:14px;align-items:center}
.partners span{display:flex;align-items:center;gap:6px;font-weight:600;font-size:13px;color:var(--navy)}
.partners i{width:12px;height:12px;background:#9aa3b3;display:inline-block}
.stats{position:absolute;left:600px;top:506px;width:560px;height:84px;background:#fff;border:1px solid var(--line);display:flex;box-shadow:0 10px 24px rgba(15,31,61,.08)}
.stat{flex:1;text-align:center;padding-top:16px;border-right:1px solid var(--line)}
.stat:last-child{border:0}
.stat b{display:block;font-size:24px;color:var(--navy);line-height:1.1}
.stat small{font-size:10px;color:var(--muted)}

/* about */
.about{top:700px;height:360px;background:var(--soft)}
.about-copy{position:absolute;left:40px;top:38px;width:520px}
.about h2{font-size:28px;line-height:1.15;color:var(--navy);margin-top:8px;font-weight:700}
.about p{color:var(--muted);margin-top:14px;max-width:420px}
.checks{display:grid;grid-template-columns:1fr 1fr;gap:8px 20px;margin-top:18px;font-size:12px;font-weight:500;max-width:440px}
.checks span{display:flex;align-items:center;gap:8px}
.about .btn{margin-top:22px}
.about-photo{left:600px;top:0;width:600px;height:360px;background:linear-gradient(135deg,#c9a989 0,#e4d6c5 45%,#8d8f96 100%)}

/* services */
.services{top:1080px;height:540px}
.services h2{font-size:26px;color:var(--navy);margin-top:6px}
.services .intro{color:var(--muted);max-width:520px;margin:8px auto 0}
.cards{position:absolute;left:40px;top:130px;width:1120px;display:grid;grid-template-columns:repeat(4,1fr);gap:16px}
.card{border:1px solid var(--line);background:#fff;height:124px;padding:18px 18px 0;display:flex;gap:12px}
.card svg{flex:none}
.card h3{font-size:13.5px;line-height:1.25;color:var(--navy);font-weight:700}
.card p{font-size:11px;color:var(--muted);margin-top:6px;line-height:1.45}
.services .btn{position:absolute;left:532px;top:418px}

/* why */
.why{top:1630px;height:300px;background:var(--navy);color:#fff}
.why-photo{left:60px;top:28px;width:400px;height:244px;background:linear-gradient(160deg,#6e8aa6 0,#a9b8c7 40%,#3d4f66 100%)}
.why-copy{position:absolute;left:530px;top:50px;width:600px}
.why h2{font-size:28px;margin-top:8px;font-weight:700}
.why p{color:#c3cad8;margin-top:12px;max-width:480px}
.feats{display:flex;gap:34px;margin-top:26px}
.feat{display:flex;flex-direction:column;align-items:center;gap:8px;color:var(--red);font-size:11px;font-weight:700;text-transform:uppercase;width:110px;text-align:center}

/* process */
.process{top:1950px;height:220px}
.process h2{font-size:26px;color:var(--navy);margin-top:6px}
.steps{position:absolute;left:40px;top:96px;width:1120px;display:flex;align-items:flex-start}
.step{flex:1}
.step b{font-size:13px;color:var(--navy);display:block}
.step b em{font-style:normal;color:var(--red);margin-right:4px}
.step p{font-size:11px;color:var(--muted);margin-top:6px;max-width:170px}
.arrow{width:36px;padding-top:4px}

/* listings */
.listings{top:2190px;height:310px}
.listings .label{position:absolute;left:40px;top:0}
.props{position:absolute;left:40px;top:26px;display:flex;gap:18px}
.prop{width:240px}
.prop .img{height:150px;position:relative}
.tag{position:absolute;left:10px;top:10px;background:var(--red);color:#fff;font-size:9px;font-weight:700;padding:3px 8px;letter-spacing:.5px}
.prop h4{font-size:13px;color:var(--navy);margin-top:10px}
.prop small{color:var(--muted);font-size:11px;display:block}
.prop .meta{display:flex;justify-content:space-between;font-size:11px;margin-top:6px;color:var(--muted)}
.prop .meta b{color:var(--red)}
.quote{position:absolute;left:820px;top:26px;width:340px;height:250px;border:1px solid var(--line);padding:24px;background:#fff}
.quote .label{position:static}
.stars{color:var(--red);font-size:14px;letter-spacing:2px}
.quote p{font-size:12px;color:var(--muted);margin-top:10px;font-style:italic}
.quote h4{font-size:13px;color:var(--navy);margin-top:14px}
.quote small{font-size:11px;color:var(--muted)}
.dots{display:flex;gap:6px;margin-top:14px}
.dots i{width:7px;height:7px;border-radius:50%;background:#cdd2db}
.dots i:first-child{background:var(--red)}

/* cta */
.cta{top:2510px;height:160px;background:#eef0f4}
.cta h2{position:absolute;left:40px;top:36px;font-size:26px;line-height:1.2;color:var(--navy);width:460px}
.cta p{position:absolute;left:40px;top:108px;color:var(--muted);width:440px;font-size:12px}
.cta .ctas{position:absolute;left:640px;top:58px;display:flex;gap:14px}

/* footer */
.footer{top:2670px;height:338px;background:var(--navy);color:#c3cad8}
.f-logo{position:absolute;left:40px;top:36px;width:110px;height:100px;border:1px solid rgba(255,255,255,.2);display:flex;flex-direction:column;align-items:center;justify-content:center;gap:6px}
.f-logo .sq{width:14px;height:14px;background:var(--red)}
.f-about{position:absolute;left:40px;top:150px;width:220px;font-size:11.5px}
.socials{position:absolute;left:40px;top:232px;display:flex;gap:8px}
.socials i{width:22px;height:22px;border-radius:50%;background:rgba(255,255,255,.15)}
.f-col{position:absolute;top:40px;font-size:12px}
.f-col h4{color:#fff;font-size:13px;margin-bottom:12px;letter-spacing:.5px;text-transform:uppercase}
.f-col li{list-style:none;margin-bottom:6px}
.f-bottom{position:absolute;left:40px;right:40px;top:292px;border-top:1px solid rgba(255,255,255,.15);padding-top:14px;font-size:11px;display:flex;justify-content:space-between}
</style>
</head>
<body>

<header class="sec header">
  <div class="logo-box"><span class="sq"></span><span class="brand">TALLGROVE<br>VALE</span></div>
  <nav class="nav">
    <a class="on">Home</a><a>Services</a><a>About Us</a><a>Properties</a><a>Resources</a><a>Contact</a>
  </nav>
  <div class="head-right">
    <span class="ico-phone"><svg width="16" height="16" viewBox="0 0 24 24"><path d="M6.6 10.8a15 15 0 0 0 6.6 6.6l2.2-2.2c.3-.3.7-.4 1-.2 1.1.4 2.3.6 3.6.6.6 0 1 .4 1 1V20c0 .6-.4 1-1 1A17 17 0 0 1 3 4c0-.6.4-1 1-1h3.5c.6 0 1 .4 1 1 0 1.3.2 2.5.6 3.6.1.3 0 .7-.2 1z" fill="#c8102e"/></svg>(555) 014-2288</span>
    <span class="btn btn-red">Get Free Consultation</span>
  </div>
</header>

<section class="sec hero">
  <div class="photo hero-photo" role="img" aria-label="Photo of a classic apartment building against a blue sky"></div>
  <div class="hero-copy">
    <span class="pill">Trusted Property Management in Ohio</span>
    <h1>Better Management.<br>Stronger Returns.<br><span>Total Peace of Mind.</span></h1>
    <p>We help property owners protect their investments with professional management, tenant screening, maintenance coordination, and transparent communication.</p>
    <div class="ctas"><span class="btn btn-red">Get Free Consultation</span><span class="btn btn-ghost">Explore Services →</span></div>
    <div class="badges"><span><i></i>Licensed &amp; Insured</span><span><i></i>Local Experts</span><span><i></i>Fast Response</span><span><i></i>Trusted by Owners</span></div>
  </div>
  <div class="trusted">
    <h4>Trusted By Property Owners</h4>
    <div class="partners"><span><i></i>Nestly</span><span><i></i>HomeRow</span><span><i></i>RentSpan</span><span><i></i>LeaseLoop</span></div>
  </div>
  <div class="stats">
    <div class="stat"><b>500+</b><small>Properties Managed</small></div>
    <div class="stat"><b>98%</b><small>Occupancy Rate</small></div>
    <div class="stat"><b>15+</b><small>Years of Experience</small></div>
    <div class="stat"><b>4.9</b><small>Client Rating</small></div>
  </div>
</section>

<section class="sec about">
  <div class="about-copy">
    <span class="label">About Tallgrove Vale Management</span>
    <h2>Property Management<br>Built Around Trust.</h2>
    <p>From marketing and tenant screening to maintenance and financial reporting, we handle everything so you can enjoy stress-free ownership.</p>
    <div class="checks">
      <span><svg width="14" height="14" viewBox="0 0 14 14"><circle cx="7" cy="7" r="7" fill="#c8102e"/><path d="M4 7l2 2 4-4" stroke="#fff" stroke-width="1.6" fill="none"/></svg>Transparent Communication</span>
      <span><svg width="14" height="14" viewBox="0 0 14 14"><circle cx="7" cy="7" r="7" fill="#c8102e"/><path d="M4 7l2 2 4-4" stroke="#fff" stroke-width="1.6" fill="none"/></svg>Financial Reporting</span>
      <span><svg width="14" height="14" viewBox="0 0 14 14"><circle cx="7" cy="7" r="7" fill="#c8102e"/><path d="M4 7l2 2 4-4" stroke="#fff" stroke-width="1.6" fill="none"/></svg>Dedicated Property Managers</span>
      <span><svg width="14" height="14" viewBox="0 0 14 14"><circle cx="7" cy="7" r="7" fill="#c8102e"/><path d="M4 7l2 2 4-4" stroke="#fff" stroke-width="1.6" fill="none"/></svg>Preventative Maintenance</span>
      <span><svg width="14" height="14" viewBox="0 0 14 14"><circle cx="7" cy="7" r="7" fill="#c8102e"/><path d="M4 7l2 2 4-4" stroke="#fff" stroke-width="1.6" fill="none"/></svg>Local Market Expertise</span>
      <span><svg width="14" height="14" viewBox="0 0 14 14"><circle cx="7" cy="7" r="7" fill="#c8102e"/><path d="M4 7l2 2 4-4" stroke="#fff" stroke-width="1.6" fill="none"/></svg>Tenant Satisfaction Focus</span>
    </div>
    <span class="btn btn-navy">Learn More About Us →</span>
  </div>
  <div class="photo about-photo" role="img" aria-label="Photo of a team meeting around a table seen from above"></div>
</section>

<section class="sec services center">
  <span class="label">Our Services</span>
  <h2>Comprehensive Property Management Solutions</h2>
  <p class="intro">From marketing and tenant screening to maintenance and financial reporting, we handle everything so you can enjoy stress-free ownership.</p>
  <div class="cards" style="text-align:left">
    <div class="card"><svg width="30" height="30" viewBox="0 0 30 30"><path d="M4 14L15 5l11 9v12H4z" fill="none" stroke="#c8102e" stroke-width="2"/></svg><div><h3>Residential Property Management</h3><p>Full-service management for single-family homes, condos and multi-family properties.</p></div></div>
    <div class="card"><svg width="30" height="30" viewBox="0 0 30 30"><rect x="6" y="4" width="18" height="22" fill="none" stroke="#c8102e" stroke-width="2"/><path d="M10 9h3M17 9h3M10 14h3M17 14h3M10 19h3M17 19h3" stroke="#c8102e" stroke-width="2"/></svg><div><h3>Commercial Property Management</h3><p>Expert management for office buildings, retail spaces and commercial properties.</p></div></div>
    <div class="card"><svg width="30" height="30" viewBox="0 0 30 30"><circle cx="15" cy="10" r="5" fill="none" stroke="#c8102e" stroke-width="2"/><path d="M5 26c1-6 5-9 10-9s9 3 10 9" fill="none" stroke="#c8102e" stroke-width="2"/></svg><div><h3>Tenant Placement</h3><p>Rigorous screening and placement to ensure quality tenants and reduced vacancy.</p></div></div>
    <div class="card"><svg width="30" height="30" viewBox="0 0 30 30"><path d="M20 4a6 6 0 0 0-6 8L5 21l4 4 9-9a6 6 0 0 0 8-6l-4 2-3-3z" fill="none" stroke="#c8102e" stroke-width="2"/></svg><div><h3>Maintenance Coordination</h3><p>24/7 maintenance support and vendor management to keep your property in top condition.</p></div></div>
    <div class="card"><svg width="30" height="30" viewBox="0 0 30 30"><rect x="4" y="8" width="22" height="15" rx="2" fill="none" stroke="#c8102e" stroke-width="2"/><circle cx="15" cy="15.5" r="3" fill="none" stroke="#c8102e" stroke-width="2"/></svg><div><h3>Rent Collection</h3><p>Online rent collection and timely payment options for convenience and accuracy.</p></div></div>
    <div class="card"><svg width="30" height="30" viewBox="0 0 30 30"><path d="M5 25h20M8 25V15M14 25V9M20 25V12" stroke="#c8102e" stroke-width="3"/></svg><div><h3>Financial Reporting</h3><p>Detailed monthly statements and record keeping for complete transparency.</p></div></div>
    <div class="card"><svg width="30" height="30" viewBox="0 0 30 30"><circle cx="13" cy="13" r="7" fill="none" stroke="#c8102e" stroke-width="2"/><path d="M18 18l7 7" stroke="#c8102e" stroke-width="2.5"/></svg><div><h3>Property Inspections</h3><p>Regular inspections to protect your investment and ensure tenant compliance.</p></div></div>
    <div class="card"><svg width="30" height="30" viewBox="0 0 30 30"><path d="M4 22l7-7 5 5 10-10" fill="none" stroke="#c8102e" stroke-width="2"/><path d="M20 10h6v6" fill="none" stroke="#c8102e" stroke-width="2"/></svg><div><h3>Investment Consulting</h3><p>Expert advice to help you make informed investment decisions.</p></div></div>
  </div>
  <span class="btn btn-navy">View All Services</span>
</section>

<section class="sec why">
  <div class="photo why-photo" role="img" aria-label="Photo of a modern building exterior with a company sign"></div>
  <div class="why-copy">
    <span class="label">Why Choose Us</span>
    <h2>Your Success is Our Priority</h2>
    <p>We combine local expertise, proven processes, and cutting-edge technology to deliver exceptional results for property owners.</p>
    <div class="feats">
      <div class="feat"><svg width="34" height="34" viewBox="0 0 34 34"><path d="M17 3l4 9 10 1-8 7 3 10-9-5-9 5 3-10-8-7 10-1z" fill="none" stroke="#c8102e" stroke-width="2"/></svg>Local Expertise</div>
      <div class="feat"><svg width="34" height="34" viewBox="0 0 34 34"><path d="M4 8h26v16H14l-6 5v-5H4z" fill="none" stroke="#c8102e" stroke-width="2"/></svg>Transparent Communication</div>
      <div class="feat"><svg width="34" height="34" viewBox="0 0 34 34"><circle cx="17" cy="12" r="6" fill="none" stroke="#c8102e" stroke-width="2"/><path d="M6 30c1-7 5-10 11-10s10 3 11 10" fill="none" stroke="#c8102e" stroke-width="2"/></svg>Dedicated Team</div>
      <div class="feat"><svg width="34" height="34" viewBox="0 0 34 34"><path d="M17 3l12 5v9c0 7-5 12-12 14C10 29 5 24 5 17V8z" fill="none" stroke="#c8102e" stroke-width="2"/><path d="M12 17l4 4 7-8" fill="none" stroke="#c8102e" stroke-width="2"/></svg>Proven Results</div>
    </div>
  </div>
</section>

<section class="sec process center">
  <span class="label">Our Process</span>
  <h2>A Simple, Proven Process</h2>
  <div class="steps" style="text-align:left">
    <div class="step"><b><em>01</em>Inquiry</b><p>Contact us to discuss your property and management needs.</p></div>
    <svg class="arrow" width="36" height="14" viewBox="0 0 36 14"><path d="M2 7h30M26 2l6 5-6 5" fill="none" stroke="#c8102e" stroke-width="2"/></svg>
    <div class="step"><b><em>02</em>Property Evaluation</b><p>We evaluate your property and provide a customized management plan.</p></div>
    <svg class="arrow" width="36" height="14" viewBox="0 0 36 14"><path d="M2 7h30M26 2l6 5-6 5" fill="none" stroke="#c8102e" stroke-width="2"/></svg>
    <div class="step"><b><em>03</em>Marketing &amp; Leasing</b><p>We market your property and place quality tenants quickly.</p></div>
    <svg class="arrow" width="36" height="14" viewBox="0 0 36 14"><path d="M2 7h30M26 2l6 5-6 5" fill="none" stroke="#c8102e" stroke-width="2"/></svg>
    <div class="step"><b><em>04</em>Management</b><p>We handle the day-to-day management so you don't have to.</p></div>
    <svg class="arrow" width="36" height="14" viewBox="0 0 36 14"><path d="M2 7h30M26 2l6 5-6 5" fill="none" stroke="#c8102e" stroke-width="2"/></svg>
    <div class="step"><b><em>05</em>Monthly Reporting</b><p>Receive detailed reports and statements every month.</p></div>
  </div>
</section>

<section class="sec listings">
  <span class="label">Featured Properties</span>
  <div class="props">
    <div class="prop"><div class="img" role="img" aria-label="Photo of a luxury apartment building" style="background:linear-gradient(160deg,#8fa8c4,#c7b39c)"><span class="tag">FOR RENT</span></div><h4>Luxury Apartment</h4><small>Columbus, OH</small><div class="meta"><span>2 Beds · 2 Baths</span><b>$1,850/month</b></div></div>
    <div class="prop"><div class="img" role="img" aria-label="Photo of a downtown condo tower" style="background:linear-gradient(160deg,#9ab3cc,#6f7f93)"><span class="tag">FOR RENT</span></div><h4>Downtown Condo</h4><small>Cleveland, OH</small><div class="meta"><span>1 Bed · 1 Bath</span><b>$1,350/month</b></div></div>
    <div class="prop"><div class="img" role="img" aria-label="Photo of a commercial office building" style="background:linear-gradient(160deg,#a7bfd6,#b9a48f)"><span class="tag">FOR SALE</span></div><h4>Commercial Building</h4><small>Dublin, OH</small><div class="meta"><span>5,400 sq ft</span><b>$950,000</b></div></div>
  </div>
  <div class="quote">
    <span class="label">Client Testimonials</span>
    <div class="stars">★★★★★</div>
    <p>"Tallgrove Vale Management has been exceptional to work with. They're responsive, professional and truly care about protecting my investment. My property has never been in better hands."</p>
    <h4>Dana K.</h4><small>Property Owner</small>
    <div class="dots"><i></i><i></i><i></i></div>
  </div>
</section>

<section class="sec cta">
  <h2>Ready to Maximize Your Property Investment?</h2>
  <p>Partner with Tallgrove Vale Management for professional, reliable, and results-driven property management.</p>
  <div class="ctas"><span class="btn btn-red">Get Free Consultation</span><span class="btn btn-ghost">Call (555) 014-2288</span></div>
</section>

<footer class="sec footer">
  <div class="f-logo"><span class="sq"></span><span class="brand">TALLGROVE<br>VALE</span></div>
  <p class="f-about">Professional property management services throughout Ohio. We protect your investment and maximize your returns.</p>
  <div class="socials"><i></i><i></i><i></i><i></i></div>
  <div class="f-col" style="left:330px"><h4>Services</h4><ul><li>Residential Management</li><li>Commercial Management</li><li>Tenant Placement</li><li>Maintenance Coordination</li><li>Financial Reporting</li><li>Property Inspections</li></ul></div>
  <div class="f-col" style="left:540px"><h4>Company</h4><ul><li>About Us</li><li>Our Team</li><li>Careers</li><li>Testimonials</li><li>Blog</li><li>Privacy Policy</li><li>Terms of Service</li></ul></div>
  <div class="f-col" style="left:720px"><h4>Resources</h4><ul><li>Owner Resources</li><li>Tenant Resources</li><li>FAQs</li><li>Investment Guide</li><li>Legal Documents</li></ul></div>
  <div class="f-col" style="left:900px"><h4>Contact Us</h4><ul><li>120 Orchard Way</li><li>Columbus, OH 43215</li><li>(555) 014-2288</li><li>info@tallgrovevalemanagement.com</li><li>Mon – Fri: 8:00 AM – 5:00 PM</li><li>Sat – Sun: Closed</li></ul></div>
  <div class="f-bottom"><span>© 2025 Tallgrove Vale Management. All rights reserved.</span><span>tallgrovevalemanagement.com</span></div>
</footer>

</body>
</html>
```